Chronicles of Kin Logo Design plus business cards design

We are a start up company that will help seniors write their memoirs...beginning with a few ancestors and their heritage and continuing through their own history...how they would like to be remembered in the next generation. I envision a card with a senior citizen at an older writing desk, writing her memoirs, with a book (maybe standing on top, leaning slightly) that has the words Chronicles of Kin.com on the back binding. OR maybe a senior couple walking into the sunset with the same book somewhere in the frame. Communicating the relevance of every life being significant to those that come after them...when a genealogy doesn't say enough about the details of ones life. Please note that I am open to the professionals own ideas...I am not locked into my concepts. On the back of the card I would like one or two phrases..."A Genealogy Doesn't Say Enough" and/or "Every life legacy is uniquely significant to the next generation".
Updates

I have added a couple of photos for ideas that may be used if needed.

I have both increased and committed the payment! Thanks for the reminder!

Reason: We increased the payment commitment and added some photo ideas to help.

We want to thank EVERYONE who participated in this contest. There were so many wonderful and VERY professional proposals...making it very challenging to decide on one! We are posting a new contest for a brochure now and hope many of you will participate. May God bless your endeavors.

Target Market(s)

Senior populous & baby boomer generation.

Industry/Entity Type

Business

Logo Text

Chronicles of Kin quiet years...lasting echoes

Requirements
Must have
• Relevant info:
Domain name: chroniclesofkin.com
email: info@chroniclesofkin.com
phone: 1-855-KIN-TALE toll free
1-717-382-6150 local
name: Doris Halvorsen, M.A.
Nice to have
• photo of senior or senior couple....book with our web address on the binding. I attached two photos that could work if cropped and enhanced. Words need to be deleted from the one photo of senior at a writing desk and couple on the beach could use a sunset sky and other people cropped out. Just ideas...don't know if you have better ones or prefer a different idea.

```html
<!DOCTYPE html>
<html lang="en">
<head>
<meta charset="utf-8">
<title>Chronicles of Kin — Business Card</title>
<link rel="stylesheet" href="https://fonts.googleapis.com/css2?family=Mrs+Saint+Delafield&family=Share+Tech+Mono&display=swap">
<style>
  :root {
    --sky-cream: #fffdf0;
    --sky-mist: #f4f8ec;
    --shore-aqua: #7fe6d6;
    --sea-teal: #15c9a8;
    --meadow-green: #2fd58a;
    --meadow-deep: #169a6a;
    --walker-slate: #2e6168;
    --walker-red: #e8284a;
    --desk-warm: #e8403a;
    --desk-gold: #f5b640;
    --desk-violet: #6b4c9a;
    --ink: #1c1c1c;
  }
  html, body {
    margin: 0;
    padding: 0;
    overflow: hidden;
    background: #ffffff;
  }
  .card {
    position: relative;
    width: 1200px;
    height: 702px;
    overflow: hidden;
    background: var(--sky-cream);
  }
  .landscape-scene {
    position: absolute;
    inset: 0;
    background:
      linear-gradient(180deg,
        var(--sky-cream) 0%,
        var(--sky-mist) 50%,
        var(--shore-aqua) 58%,
        var(--sea-teal) 66%,
        var(--meadow-green) 80%,
        var(--meadow-deep) 100%);
  }
  .walking-couple {
    position: absolute;
    left: 450px;
    top: 420px;
    width: 330px;
    height: 282px;
    background: linear-gradient(90deg, var(--walker-slate) 0%, var(--walker-red) 100%);
  }
  .desk-vignette {
    position: absolute;
    left: 466px;
    top: 72px;
    width: 214px;
    height: 214px;
    border-radius: 50%;
    background: radial-gradient(circle at 40% 55%,
      var(--desk-gold) 0%,
      var(--desk-warm) 40%,
      var(--desk-violet) 75%,
      #f3e6d8 100%);
  }
  .brand-name {
    position: absolute;
    left: 0;
    right: 0;
    top: 222px;
    margin: 0;
    text-align: center;
    font-family: "Mrs Saint Delafield", cursive;
    font-weight: 400;
    font-size: 146px;
    line-height: 1;
    color: var(--ink);
    letter-spacing: 12px;
  }
  .contact {
    position: absolute;
    left: 75px;
    top: 494px;
    margin: 0;
    font-family: "Share Tech Mono", monospace;
    font-style: normal;
    color: var(--ink);
  }
  .contact-name {
    margin: 0 0 4px;
    font-size: 22px;
    font-weight: 400;
    letter-spacing: 2px;
    -webkit-text-stroke: 0.6px var(--ink);
  }
  .contact-line {
    display: block;
    font-size: 20px;
    line-height: 27px;
    letter-spacing: 0.6px;
  }
</style>
</head>
<body>
  <main class="card">
    <div class="landscape-scene" role="img" aria-label="Painterly seaside landscape with pale sky, turquoise water and green meadow"></div>
    <div class="walking-couple" role="img" aria-label="Senior couple seen from behind walking toward the sea"></div>
    <div class="desk-vignette" role="img" aria-label="Round painted vignette of a senior writing at an old desk"></div>

    <h1 class="brand-name">Chronicles of Kin</h1>

    <address class="contact">
      <p class="contact-name">DORIS HALVORSEN, M.A.,</p>
      <span class="contact-line">1-855-KIN-TALE toll free</span>
      <span class="contact-line">1-717-382-6150 local</span>
      <span class="contact-line">info@chroniclesofkin.com</span>
      <span class="contact-line">www.chroniclesofkin.com</span>
    </address>
  </main>
</body>
</html>
```